Crash repair flyer design

We need a basic flyer to distribute to potential clients and insurance companies. The design should be professional looking, uncluttered and to the point. Title should be 'Iron Ridge Panel Works' and be in a dark blue font. It should have a few pictures, some facts and a brief description of the business. Information can be taken from our website 'ironridgepanelworks.com.au'

Target Market(s)

insurance companies and general

Industry/Entity Type

Insurance

Requirements
Must have
• Company Logo
"for all your crash repair needs" to be placed somewhere.
'KLV Approved'
BGN Approved'
'ROVER SA Approved'
Nice to have
• picture of the front of the building.
picture of car being painted in the spraybooth
Should not have
• Not too may colors

```html
<!DOCTYPE html>
<html lang="en">
<head>
<meta charset="utf-8">
<title>Iron Ridge Panel Works – Flyer</title>
<link rel="stylesheet" href="https://fonts.googleapis.com/css2?family=Open+Sans:ital,wght@0,400;0,700;1,400;1,700&display=swap">
<style>
:root{
  --bg:#d3d3d3;
  --paper:#ffffff;
  --navy:#123a7a;
  --blue:#1d5f9f;
  --sky:#5bb6e8;
  --mist:#dfe7ee;
  --band:#c8dbe8;
  --ink:#222;
  --dark:#111;
  --brand-red:#c8282c;
  --grey-bar:rgba(110,110,110,.75);
}
*{margin:0;padding:0;box-sizing:border-box}
html,body{width:1200px;height:757px;overflow:hidden;background:var(--bg);font-family:"Open Sans",Arial,sans-serif}
.canvas{position:relative;width:1200px;height:757px}
.page{position:absolute;background:var(--paper);overflow:hidden}
.page--front{left:208px;top:101px;width:370px;height:524px}
.page--back{left:637px;top:98px;width:369px;height:523px}
.page__shapes{position:absolute;inset:0}
.brand{position:absolute;display:flex;align-items:center;gap:6px;font-weight:700;font-size:13px;color:var(--navy);font-family:"Open Sans",Arial,sans-serif}
.brand__dot{width:14px;height:14px;border-radius:50%;background:var(--brand-red)}
.title{position:absolute;font-weight:700;font-style:italic;color:var(--blue);letter-spacing:.5px;white-space:nowrap}
.photo{position:absolute}
.quote{position:absolute;background:var(--grey-bar);color:#fff;font-style:italic;display:flex;align-items:center;padding-left:12px}
.badge{position:absolute}
.about{position:absolute;left:11px;top:276px;width:350px}
.about__heading{font-size:11px;font-weight:700;font-style:italic;color:var(--blue);margin-bottom:4px}
.about p{font-size:7px;line-height:9px;color:var(--ink);margin:0 0 7px 10px}
.contact{position:absolute;left:200px;top:448px;width:160px;color:#fff;font-size:6.3px;line-height:8.2px}
.contact__heading{font-weight:700;font-style:italic;text-align:center;font-size:7px;margin-bottom:3px}
.contact__names{text-align:center;margin-bottom:1px}
</style>
</head>
<body>
<div class="canvas">

  <!-- Front page -->
  <section class="page page--front">
    <svg class="page__shapes" width="370" height="524" viewBox="0 0 370 524">
      <defs>
        <linearGradient id="fBand" x1="0" x2="1"><stop offset="0" stop-color="#b9d3e4"/><stop offset="1" stop-color="#e6eef4"/></linearGradient>
        <linearGradient id="fDark" x1="0" x2="1"><stop offset="0" stop-color="#000"/><stop offset="1" stop-color="#8a8a8a"/></linearGradient>
        <linearGradient id="fPhoto" x1="0" y1="0" x2="0" y2="1"><stop offset="0" stop-color="#d7dade"/><stop offset=".35" stop-color="#e9eaec"/><stop offset=".55" stop-color="#6f7479"/><stop offset="1" stop-color="#8c8d8e"/></linearGradient>
      </defs>
      <polygon points="200,0 370,0 370,91 160,91" fill="var(--mist)"/>
      <polygon points="195,0 207,0 164,91 150,91" fill="var(--navy)"/>
      <rect x="0" y="91" width="370" height="40" fill="url(#fBand)"/>
      <rect x="0" y="91" width="55" height="40" fill="#d5e4ee"/>
      <rect x="0" y="422" width="370" height="102" fill="#fff"/>
      <polygon points="150,435 370,435 370,524 88,524" fill="#a8d5ef"/>
      <polygon points="168,435 370,435 370,524 112,524" fill="var(--sky)"/>
      <polygon points="190,445 370,445 370,524 130,524" fill="url(#fDark)"/>
      <rect x="140" y="483" width="230" height="7" fill="#fff"/>
      <rect x="125" y="500" width="245" height="7" fill="#fff"/>
      <rect x="0" y="499" width="80" height="3" fill="var(--sky)"/>
      <rect x="0" y="506" width="70" height="3" fill="var(--sky)"/>
    </svg>
    <div class="brand" style="left:24px;top:42px"><span class="brand__dot"></span>IRON RIDGE</div>
    <div class="title" style="left:67px;top:102px;font-size:20px">IRON RIDGE PANEL WORKS</div>
    <div class="photo" role="img" aria-label="Photo of the workshop front with customer car parking" style="left:0;top:137px;width:370px;height:272px;background:linear-gradient(180deg,#d7dade 0%,#eceef0 30%,#8d9296 45%,#5e6266 62%,#8e8f90 100%)"></div>
    <div class="quote" style="left:0;top:374px;width:370px;height:25px;font-size:16px">"for all your crash repair needs"</div>
    <div class="badge" role="img" aria-label="Partner approval badge" style="left:13px;top:426px;width:42px;height:48px;background:#f7d117"></div>
    <div class="badge" role="img" aria-label="Association member badge" style="left:64px;top:426px;width:47px;height:48px;background:#1f5fa8"></div>
  </section>

  <!-- Back page -->
  <section class="page page--back">
    <svg class="page__shapes" width="369" height="523" viewBox="0 0 369 523">
      <defs>
        <linearGradient id="bBand" x1="0" x2="1"><stop offset="0" stop-color="#e2ecf3"/><stop offset="1" stop-color="#b9cde0"/></linearGradient>
        <linearGradient id="bDark" x1="0" x2="1"><stop offset="0" stop-color="#000"/><stop offset="1" stop-color="#9a9a9a"/></linearGradient>
        <linearGradient id="bBody" x1="0" y1="0" x2="0" y2="1"><stop offset="0" stop-color="#eef2f5"/><stop offset="1" stop-color="#fff"/></linearGradient>
      </defs>
      <polygon points="230,0 369,0 369,70 155,70" fill="var(--mist)"/>
      <polygon points="225,0 238,0 165,68 150,68" fill="var(--navy)"/>
      <rect x="0" y="68" width="155" height="4" fill="var(--sky)"/>
      <rect x="0" y="90" width="369" height="47" fill="url(#bBand)"/>
      <rect x="0" y="137" width="369" height="290" fill="url(#bBody)"/>
      <rect x="0" y="430" width="369" height="93" fill="#fff"/>
      <rect x="0" y="434" width="369" height="9" fill="var(--navy)"/>
      <polygon points="0,443 369,443 369,523 0,523" fill="#fff"/>
      <polygon points="100,440 190,440 120,523 70,523" fill="#a8d5ef"/>
      <polygon points="130,440 200,440 130,523 95,523" fill="var(--sky)"/>
      <polygon points="180,442 369,442 369,523 115,523" fill="url(#bDark)"/>
      <rect x="0" y="498" width="85" height="3" fill="var(--sky)"/>
      <rect x="0" y="505" width="75" height="3" fill="var(--sky)"/>
    </svg>
    <div class="brand" style="left:42px;top:30px"><span class="brand__dot"></span>IRON RIDGE</div>
    <div class="title" style="left:186px;top:51px;font-size:12.5px">IRON RIDGE PANEL WORKS</div>
    <div class="photo" role="img" aria-label="Car masked in pink paper inside the spray booth" style="left:0;top:134px;width:110px;height:98px;background:linear-gradient(160deg,#d9dde0,#8b9296 50%,#c9a4a8);border:2px solid #8fc8e6"></div>
    <div class="photo" role="img" aria-label="Photo of a car being painted in the spray booth" style="left:234px;top:137px;width:135px;height:107px;background:linear-gradient(180deg,#d8dadc,#9ea3a7 60%,#6a6f73);border:2px solid #8fc8e6"></div>
    <div class="photo" role="img" aria-label="SUV parked in the brightly lit spray booth" style="left:110px;top:165px;width:136px;height:101px;background:linear-gradient(180deg,#eef0f1,#b5babd 55%,#6a6f73);border:2px solid #8fc8e6"></div>
    <div class="about">
      <div class="about__heading">IRON RIDGE PANEL WORKS</div>
      <p>Ensures customer satisfaction; we have a team of qualified trade technicians that take the time to ensure a job well done. Your family's safety and well being is important to us.</p>
      <p>Family owned business over 31 years of experience. Constantly expanding and improving. Dedicated to improving quality and service.</p>
    </div>
    <div class="quote" style="left:0;top:375px;width:369px;height:22px;font-size:14px">"for all your crash repair needs"</div>
    <div class="badge" role="img" aria-label="Quality approved member certificate" style="left:39px;top:434px;width:31px;height:50px;background:#1c8c7e"></div>
    <div class="contact">
      <div class="contact__heading">Contact Details:</div>
      <div class="contact__names">Daniel or Mark Harlow</div>
      <div>Address: 42 Kestrel Road, Marwood, S.A. 5099</div>
      <div>Phone No: (08) 8360 1172</div>
      <div>Fax: (08) 8360 1175</div>
      <div>Email: &nbsp; admin@ironridgepanelworks.com.au</div>
    </div>
  </section>

</div>
</body>
</html>
```